Product label for herbal salves, lotions, soaps and tinctures

We need a very simple, clean and organic looking label that can be used for an ointment jar, a lotion bottle and a dropper bottle.
We have an existing logo (see attached). We like the colors white, olive green, gold and black. It needs to include product name as dominant and logo. It also needs to include an ingredient list, and usage statement. Include weight of product, distributed by, made in the USA, and NQB statement.
Example of what needs to be present:
Logo
Name: Calmwick Balm
Used for: For Muscle Aches, Arthritis, Tendonitis, Headaches
To Use: For muscle aches, arthritis and tendonitis, massage into affected area. For tension headache apply to neck, temples and forehead.
Store in a cool and dry place, away from direct heat and sunlight.
Weight of product: 1.75
DIST. BY: Brookmere Herbal
Made in the USA
This product is not intended to diagnose, treat, cure
or prevent any disease. Not regulated
by the NQB. Please consult your health care practitioner
before using product. Discontinue use if any adverse reaction occurs.
Ingredient list:
Wildcrafted Ingredients:
Ashwagandha Root, Peppermint Leaf, Hops Flowers, St. John’s Wort Herb, Arnica Flowers, Green Tea Leaf, Alfalfa Leaf, Dandelion Root, Burdock Root, Chickweed Herb, Chaparral Leaf, Yarrow Flowers, Boneset Herb, Moringa Leaf, Meadowsweet Herb, Nettle Leaf
Organic Ingredients:
Olive Oil, Aloe Leaf, Sweet Birch Bark, Helichrysum Flowers, Holy Basil Leaf, Borage Herb, Ginger Root, Angelica Root, White Willow Bark, Mustard Seed, Beeswax, Vitamin E, Essential Oils
Dimensions of Jar:
Circumference: 7 in.
Height: 1 in.

```html
<!DOCTYPE html>
<html lang="en">
<head>
<meta charset="utf-8">
<title>Calmwick Balm – Jar Label</title>
<link href="https://fonts.googleapis.com/css2?family=Bitter:wght@700&family=Open+Sans:wght@400;600;700&display=swap" rel="stylesheet">
<style>
  :root {
    --backdrop: #d2952e;
    --label-white: #ffffff;
    --gold: #c98d26;
    --olive: #6b7030;
    --olive-light: #c9cfa4;
    --ink: #1a1a1a;
  }
  * { margin: 0; padding: 0; box-sizing: border-box; }
  html, body { width: 1200px; height: 600px; overflow: hidden; }
  body {
    background: var(--backdrop);
    font-family: "Open Sans", sans-serif;
    color: var(--ink);
    position: relative;
  }
  .label {
    position: absolute;
    left: 20px; top: 218px;
    width: 1160px; height: 164px;
    background: var(--label-white);
    overflow: hidden;
  }
  .botanical-border {
    position: absolute;
    left: 350px; top: 112px;
    width: 515px; height: 52px;
    background: linear-gradient(180deg, rgba(201,207,164,0) 0%, rgba(201,207,164,0.45) 60%, rgba(201,207,164,0.6) 100%);
    z-index: 0;
  }
  .ingredients, .distributor, .storage-note, .brand, .product-name,
  .uses-band, .net-weight, .directions { z-index: 1; }
  .ingredients {
    position: absolute;
    left: 67px; top: 10px;
    font-size: 8.7px;
    line-height: 10.9px;
    white-space: nowrap;
  }
  .ingredients .heading { color: var(--olive); font-weight: 600; }
  .ingredients .group { color: var(--gold); font-weight: 600; }
  .distributor {
    position: absolute;
    left: 67px; top: 124px;
    font-size: 8.7px;
    line-height: 10.9px;
    white-space: nowrap;
  }
  .distributor strong { font-weight: 600; }
  .storage-note {
    position: absolute;
    left: 160px; top: 125px;
    border: 1px solid var(--olive);
    font-size: 8.4px;
    line-height: 10.9px;
    font-weight: 600;
    padding: 2px 4px;
    white-space: nowrap;
  }
  .brand {
    position: absolute;
    left: 444px; top: 42px;
    display: flex; align-items: center; gap: 7px;
  }
  .brand-dot {
    width: 12px; height: 12px; border-radius: 50%;
    background: var(--olive); flex: none;
  }
  .brand-name {
    font-family: "Bitter", serif;
    font-weight: 700;
    color: var(--olive);
    font-size: 22px;
    line-height: 25px;
    white-space: nowrap;
  }
  .product-name {
    position: absolute;
    left: 589px; top: 22px;
    font-family: "Bitter", serif;
    font-weight: 700;
    color: var(--gold);
    font-size: 37px;
    line-height: 34px;
    letter-spacing: 1.5px;
  }
  .uses-band {
    position: absolute;
    left: 589px; top: 94px;
    width: 232px; height: 13px;
    background: var(--olive);
    color: var(--label-white);
    font-size: 9.4px; line-height: 13px;
    font-weight: 600;
    padding-left: 4px;
    white-space: nowrap;
  }
  .net-weight {
    position: absolute;
    left: 590px; top: 110px;
    font-size: 9.6px;
    font-weight: 600;
  }
  .directions {
    position: absolute;
    left: 871px; top: 10px;
    font-size: 8.7px;
    line-height: 10.9px;
    white-space: nowrap;
  }
  .directions .heading { color: var(--gold); }
  .directions .usage { font-weight: 700; margin-bottom: 6px; }
</style>
</head>
<body>
  <section class="label">
    <div class="botanical-border" role="img" aria-label="Line-drawn olive branches and leaves along the lower edge"></div>

    <div class="ingredients">
      <p class="heading">Ingredient list:</p>
      <p class="group">Wildcrafted Ingredients:</p>
      <p>Ashwagandha Root, Peppermint Leaf, Hops Flowers, St. John’s Wort Herb,<br>Arnica Flowers, Green Tea Leaf, Alfalfa Leaf, Dandelion Root, Burdock Root,<br>Chickweed Herb, Chaparral Leaf, Yarrow Flowers, Boneset Herb, Moringa Leaf,<br>Meadowsweet Herb, Nettle Leaf</p>
      <p class="group">Organic Ingredients:</p>
      <p>Olive Oil, Aloe Leaf, Sweet Birch Bark, Helichrysum Flowers, Holy Basil Leaf,<br>Borage Herb, Ginger Root, Angelica Root, White Willow Bark, Mustard Seed,<br>Beeswax, Vitamin E, Essential Oils</p>
    </div>

    <div class="distributor">
      <p>Distributed by:</p>
      <p><strong>Brookmere Herbal</strong></p>
      <p><strong>Made in the USA</strong></p>
    </div>

    <div class="storage-note">Store in a cool and dry place,<br>away from direct heat and sunlight.</div>

    <div class="brand">
      <span class="brand-dot"></span>
      <span class="brand-name">Brookmere<br>Herbal</span>
    </div>

    <h1 class="product-name">Calmwick<br>Balm</h1>
    <p class="uses-band">Muscle Aches, Arthritis, Tendonitis, Headache</p>
    <p class="net-weight">1.75 oz</p>

    <div class="directions">
      <p class="heading">How to Use :</p>
      <p class="usage">For muscle aches, arthritis and tendonitis,<br>massage into affected area.<br>For tension headache apply to neck, temples and<br>forehead.</p>
      <p>This product is not intended to diagnose, treat, cure<br>or prevent any disease.<br>Not regulated by the NQB.<br>Please consult your health care practitioner<br>before using product.<br>Discontinue use if any adverse reaction occurs.</p>
    </div>
  </section>
</body>
</html>
```